Visitenkarten für Containerhandel
BROV
alles tip top wie bestellt so wurde geliefert!
Zielgruppe
Wir handeln mit See und Lagercontainer
Aufgabenstellung
evtl. Das Seecontainer Designe integrieren
Angaben auf der Karte;
//Frimenangaben//
TORVELMARK AG
Ribelweg 27
CH - 4912 Halvenbach
sales@torvelmark.ch
//Personenangaben//
Lukas Brenni
Leiter Verkauf

```html
<!DOCTYPE html>
<html lang="de">
<head>
<meta charset="utf-8">
<title>TORVELMARK AG – Visitenkarten</title>
<link rel="stylesheet" href="https://fonts.googleapis.com/css2?family=Mulish:wght@300;400;800&display=swap">
<style>
  :root {
    --backdrop: #c3dff2;
    --card: #ffffff;
    --navy: #15215f;
    --ink: #111111;
    --shadow: rgba(20, 40, 70, 0.22);
  }
  * { margin: 0; padding: 0; box-sizing: border-box; }
  html, body {
    width: 1200px; height: 873px; overflow: hidden;
    background: var(--backdrop);
    font-family: "Mulish", Arial, sans-serif;
    color: var(--ink);
  }
  .canvas {
    position: relative; width: 1200px; height: 873px;
    display: flex; justify-content: center; align-items: center; gap: 60px;
  }
  .card {
    position: relative; width: 510px; height: 330px;
    background: var(--card);
    box-shadow: 0 14px 30px var(--shadow);
    overflow: hidden;
  }

  /* Contact side */
  .card-contact .brand-band {
    position: absolute; left: 0; top: 0; width: 100%; height: 86px;
    background: var(--navy);
    display: flex; align-items: center; padding-left: 34px;
  }
  .brand-band .wordmark {
    color: #fff; font-weight: 800; font-size: 24px; letter-spacing: 1px;
  }
  .person {
    position: absolute; left: 34px; top: 110px;
  }
  .person .name { font-weight: 800; font-size: 24px; line-height: 1.15; }
  .person .role { font-weight: 300; font-size: 15px; margin-top: 2px; }
  .contact-lines {
    position: absolute; left: 34px; top: 194px;
    font-size: 15px; font-weight: 400; line-height: 1.5;
  }
  .company-address {
    position: absolute; left: 286px; top: 222px;
    font-size: 17px; font-weight: 400; line-height: 1.45;
    font-style: normal;
  }

  /* Brand side */
  .card-brand {
    display: flex; align-items: center; justify-content: center; gap: 18px;
  }
  .card-brand .wordmark {
    color: var(--ink); font-weight: 800; font-size: 50px; letter-spacing: 1px;
  }
  .card-brand .brand-square {
    width: 54px; height: 54px; background: var(--navy);
  }
</style>
</head>
<body>
  <main class="canvas">
    <section class="card card-contact" aria-label="Visitenkarte Rückseite">
      <div class="brand-band"><span class="wordmark">TORVELMARK</span></div>
      <div class="person">
        <p class="name">Lukas Brenni</p>
        <p class="role">Leiter Verkauf</p>
      </div>
      <div class="contact-lines">
        <p>+41 58 204 71 63</p>
        <p>sales@torvelmark.ch</p>
        <p>www.torvelmark.ch</p>
      </div>
      <address class="company-address">
        <p>TORVELMARK AG</p>
        <p>Ribelweg 27</p>
        <p>CH - 4912 Halvenbach</p>
      </address>
    </section>

    <section class="card card-brand" aria-label="Visitenkarte Vorderseite">
      <span class="wordmark">TORVELMARK</span>
      <span class="brand-square"></span>
    </section>
  </main>
</body>
</html>
```